STRIDE TOWARD WELLNESS 1K/5K WALK/RUN HEALTH EXPO

NEED A HEALTH FAIR FLYER EMPHASIZING THE WALK AS WELL AS ALL HEALTH FAIR. MY VISION IS TO HAVE SOMEONE RUNNING WITH VARIOUS HEALTH CONDITIONS INSIDE THE BRAIN . AS MANY HEALTH CONDITIONS AS POSSIBLE SUCH AS HEART DISEASE, DIABETES, MENTAL HEALTH, AND AS MANY THAT CAN FIT IN THE BRAIN. THE HAIR CAN ALSO HAVE THE COLORS THAT REPRESENT THE HEALTH CONDITION. Eg. Pink represents breast cancer; red represent heart disease, mental Health is green
Details: Corbel Sisters Circle 1k/5k Health Expo
Date: 3/25/2023
Time: 8am - 1:00 PM (8am Check in/ Walk Starts at 9:00
Location: Willowcrest Park, Duncanville TX
Theme: Stride Toward Wellness (We are bringing awareness to all health issues that are affecting our community
We would like everyone to wear the color in which they would like to bring awareness to. Eg. Pink for Breast Cancer
Green for Mental Health.)
Agenda: 8am Checkin
9am walk starts
10am-12 Music, Food, Fun, Prizes and Health Experts from the community : Working on Special Guest: Hoop Hound to lead the walk: Trying to get the Pinebrook Spirit Squad
12-1: Closing Ceremony and Breakdown

```html
<!DOCTYPE html>
<html lang="en">
<head>
<meta charset="utf-8">
<title>Stride Toward Wellness 1K/5K Walk/Run Health Expo</title>
<link rel="stylesheet" href="https://fonts.googleapis.com/css2?family=Oswald:wght@600;700&family=Roboto+Condensed:wght@700&family=Roboto:wght@700;900&family=Lilita+One&display=swap">
<style>
  :root {
    --crimson: #a01f29;
    --crimson-deep: #8f1a22;
    --ink: #111111;
    --white: #ffffff;
    --gold: #e2b457;
    --gold-light: #f3d796;
    --sky-top: #8fc3e4;
    --sky-low: #eaf4fa;
    --grass: #8cc04a;
    --track: #b3473f;
    --track-dark: #973a33;
    --brain-pink: #f2a5a0;
    --light-green: #2fa84a;
    --light-red: #e11f26;
    --light-pink: #f1a09a;
  }
  * { box-sizing: border-box; margin: 0; padding: 0; }
  html, body { width: 927px; height: 1200px; overflow: hidden; background: var(--white); }
  .flyer {
    position: relative; width: 927px; height: 1200px; overflow: hidden;
    font-family: "Roboto", Arial, sans-serif; color: var(--ink);
  }
  .backdrop {
    position: absolute; inset: 0;
    background: linear-gradient(180deg, var(--sky-top) 0%, #bcdcf0 35%, var(--sky-low) 62%, var(--sky-low) 65%,
      var(--grass) 65.2%, var(--grass) 68.5%, var(--track) 68.6%, var(--track-dark) 86%);
  }
  .chapter-name {
    position: absolute; left: 53px; top: 128px; width: 288px;
    font-family: "Oswald", sans-serif; font-weight: 700; font-size: 34px; line-height: 1.05;
    color: var(--crimson); text-align: center; text-transform: uppercase;
  }
  .headline { position: absolute; left: 275px; top: 84px; width: 600px; text-align: center; }
  .headline .event-type {
    font-family: "Oswald", sans-serif; font-weight: 700; font-size: 46px; letter-spacing: .5px;
    color: var(--crimson); line-height: 1.2;
  }
  .headline .host, .headline .expo {
    font-family: "Roboto Condensed", sans-serif; font-weight: 700; font-size: 40px; line-height: 1.38;
  }
  .when {
    position: absolute; left: 0; width: 927px; top: 302px; text-align: center;
    font-family: "Roboto Condensed", sans-serif; font-weight: 700; font-size: 36px; color: var(--crimson);
  }
  .details {
    position: absolute; left: 180px; width: 600px; top: 358px; text-align: center;
    font-weight: 700; font-size: 22px; line-height: 34px;
  }
  .mascot {
    position: absolute; left: 92px; top: 528px; width: 410px; height: 472px;
    border-radius: 46% 46% 30% 30%; background: radial-gradient(circle at 50% 35%, #f7bcb7, var(--brain-pink) 70%);
  }
  .theme-title { position: absolute; left: 20px; top: 440px; width: 540px; height: 150px; z-index: 3; }
  .theme-title text {
    font-family: "Lilita One", sans-serif; font-size: 50px; fill: var(--crimson-deep);
    stroke: var(--white); stroke-width: 5px; paint-order: stroke; stroke-linejoin: round;
  }
  .agenda {
    position: absolute; left: 538px; top: 560px; width: 368px; height: 319px;
    border-radius: 24px; background: var(--crimson-deep); color: var(--white); padding: 20px 22px;
  }
  .agenda h2 { font-weight: 900; font-size: 21px; letter-spacing: .5px; margin-top: 4px; }
  .agenda ul { list-style: none; margin-top: 10px; }
  .agenda li {
    position: relative; padding-left: 24px; font-weight: 700; font-size: 17px; line-height: 28.8px;
  }
  .agenda li::before {
    content: ""; position: absolute; left: 2px; top: 9px; width: 11px; height: 11px;
    border-radius: 50%; background: var(--gold);
  }
  .agenda .note { font-size: 9.5px; font-weight: 700; padding-left: 24px; margin-top: -4px; }
  .free-badge { position: absolute; left: 762px; top: 566px; width: 110px; height: 110px; }
  .free-badge text { font-family: "Roboto", sans-serif; font-weight: 900; font-size: 16px; fill: var(--ink); }
  .footer-band { position: absolute; left: 0; top: 1010px; width: 927px; height: 190px; }
  .signal { position: absolute; left: 696px; top: 879px; width: 44px; height: 170px; z-index: 2; }
  .mascot-small {
    position: absolute; left: 212px; top: 1030px; width: 112px; height: 150px;
    border-radius: 46% 46% 34% 34%; background: var(--brain-pink); z-index: 2;
  }
  .contact {
    position: absolute; left: 360px; width: 500px; top: 1092px; text-align: right;
    font-weight: 700; font-size: 20px; line-height: 34px;
  }
  .contact .web { color: var(--crimson); }
</style>
</head>
<body>
<main class="flyer">
  <div class="backdrop" role="img" aria-label="Illustrated blue sky with soft clouds over a green field and a red running track"></div>

  <div class="chapter-name">Corbel Sisters Circle</div>

  <header class="headline">
    <h1 class="event-type">WALK / RUN HEALTH FAIR</h1>
    <p class="host">Corbel Sisters Circle</p>
    <p class="expo">1k/5k Health Expo</p>
  </header>

  <p class="when">Date: 3/25/2023 Time: 8am - 1:00 PM</p>

  <div class="details">
    <p>8 am Check in/ Walk Starts at 9:00</p>
    <p>Location : Willowcrest Park, Duncanville TX</p>
  </div>

  <div class="mascot" role="img" aria-label="Cartoon brain character crouched at a starting line, labeled with health conditions such as mental health, heart disease, diabetes, cancer, anxiety and injuries"></div>

  <svg class="theme-title" viewBox="0 0 540 150" aria-label="Stride Toward Wellness">
    <path id="theme-arc" d="M22,128 Q270,20 522,110" fill="none"/>
    <text><textPath href="#theme-arc" startOffset="50%" text-anchor="middle">Stride Toward Wellness</textPath></text>
  </svg>

  <section class="agenda">
    <h2>AGENDA</h2>
    <ul>
      <li>8 am Checkin</li>
      <li>9 am walk starts</li>
      <li>10 am-12 Music, Food, Fun, Prizes</li>
      <li>12-1: Closing Ceremony</li>
      <li>Health Experts from the community</li>
      <li>Special Guest</li>
      <li>Vaccine Clinic</li>
      <li>Attire: Awareness Color</li>
    </ul>
    <p class="note">(Eg. Green for Mental Health, Red for Heart and Pink for Cancer)</p>
  </section>

  <svg class="free-badge" viewBox="0 0 106 106">
    <circle cx="53" cy="53" r="50" fill="var(--gold)"/>
    <circle cx="53" cy="53" r="38" fill="var(--gold-light)"/>
    <g transform="rotate(-18 53 53)">
      <text x="53" y="50" text-anchor="middle">FREE</text>
      <text x="53" y="67" text-anchor="middle" font-size="13">EVENT</text>
    </g>
  </svg>

  <svg class="footer-band" viewBox="0 0 927 190" preserveAspectRatio="none">
    <defs>
      <linearGradient id="gold-sheen" x1="0" y1="0" x2="1" y2="0">
        <stop offset="0" stop-color="#c99a3e"/>
        <stop offset=".5" stop-color="var(--gold-light)"/>
        <stop offset="1" stop-color="#d4a54a"/>
      </linearGradient>
    </defs>
    <path d="M0,40 Q463,0 927,30 L927,190 L0,190 Z" fill="url(#gold-sheen)"/>
  </svg>

  <svg class="signal" viewBox="0 0 44 170">
    <rect x="20" y="0" width="4" height="170" fill="var(--white)"/>
    <circle cx="22" cy="36" r="18" fill="var(--light-green)" stroke="var(--white)" stroke-width="3"/>
    <circle cx="22" cy="86" r="18" fill="var(--light-red)" stroke="var(--white)" stroke-width="3"/>
    <circle cx="22" cy="136" r="18" fill="var(--light-pink)" stroke="var(--white)" stroke-width="3"/>
  </svg>

  <div class="mascot-small" role="img" aria-label="Small cartoon brain character waving"></div>

  <div class="contact">
    <p>240 Larkspur Lane, Duncanville, TX 75116.</p>
    <p class="web">www.corbelsisterscircle.org</p>
  </div>
</main>
</body>
</html>
```